Powerpoint master slides for business

Hello everyone,

I am looking for a new PowerPoint master slide that should be modern, slim and yet suitable for business.

I have uploaded a few pictures, which should serve as A. orientation for my presentation. A logo should be placed on the right-hand side of the cover sheet and all subsequent slides - please insert a placeholder here. Also attached are our company colors, which must be taken into account.

Basically, I would find 6 to 10 slides (cover sheet, classic slide, end, etc.) good.

PS: The slides are intended for general everyday work, ie the design should be subtle and easily adaptable to different situations, but still look chic, modern and classy.

```html
<!DOCTYPE html>
<html lang="en">
<head>
<meta charset="utf-8">
<title>Business Master Slides</title>
<link href="https://fonts.googleapis.com/css2?family=Montserrat:wght@300;400;500;700;800&display=swap" rel="stylesheet">
<style>
:root{
  --bg:#cfe0f4;
  --navy:#1d2f6f;
  --ink:#222222;
  --dark:#242424;
  --yellow:#f8bf14;
  --deep:#0e3150;
  --grey:#666666;
  --white:#ffffff;
  --sky:linear-gradient(180deg,#c9d6e3 0%,#aebdcc 45%,#5d6d80 75%,#3b4757 100%);
  --hall:linear-gradient(180deg,#3e4652 0%,#8a929b 45%,#c9cdd1 70%,#6f6a60 100%);
}
*{margin:0;padding:0;box-sizing:border-box}
html,body{width:1200px;height:1200px;overflow:hidden}
body{background:var(--bg);font-family:"Montserrat",sans-serif;position:relative;color:var(--ink)}
.slide{position:absolute;width:520px;height:293px;background:var(--white);overflow:hidden;box-shadow:0 3px 8px rgba(30,50,90,.18)}
.abs{position:absolute}
.photo{position:absolute;background:var(--sky)}
.header-title{position:absolute;left:16px;top:13px;font-weight:700;font-size:15px;color:var(--navy);letter-spacing:.3px}
.header-title::before{content:"/";font-style:italic;color:var(--ink);margin-right:6px;font-weight:800}
.header-rule{position:absolute;left:28px;top:32px;width:474px;height:1px;background:var(--ink)}
.header-rule::after{content:"";position:absolute;right:-2px;top:-2px;width:5px;height:5px;background:var(--ink)}
.dots{position:absolute;width:74px;height:10px;background-image:radial-gradient(circle,var(--ink) 0.8px,transparent 1.1px);background-size:6.2px 5px}
.footer{position:absolute;left:0;bottom:0;width:100%;height:36px;background:var(--dark)}
.footer::before{content:"";position:absolute;left:0;top:-3px;width:100%;height:4px;background-image:radial-gradient(circle at 50% 100%,var(--dark) 1.2px,transparent 1.6px);background-size:4px 4px}
.footer .logo-text{position:absolute;left:16px;top:6px;font-weight:300;font-size:18px;color:var(--white)}
.footer .page-no{position:absolute;right:16px;top:15px;font-size:5px;color:var(--white)}
.body-text{font-size:7.2px;line-height:1.55;color:#444}
.tiny{font-size:5.6px;line-height:1.5;color:#555}
/* cover */
.cover-title{position:absolute;left:30px;top:184px;font-weight:700;font-size:31px;color:var(--navy);line-height:1}
.cover-sub{position:absolute;left:30px;top:221px;font-weight:700;font-size:21px;color:var(--navy)}
.logo-box{position:absolute;left:366px;top:205px;width:111px;height:88px;background:var(--dark);color:var(--white);font-weight:300;font-size:28px;display:flex;align-items:center;justify-content:center}
/* grid slide */
.tile-grid{position:absolute;left:52px;top:58px;width:416px;height:177px;display:grid;grid-template-columns:repeat(4,1fr);grid-template-rows:1fr 1fr}
.tile{position:relative;display:flex;flex-direction:column;align-items:center;justify-content:center;text-align:center;padding:0 8px}
.tile.is-yellow{background:var(--yellow)}
.tile.is-white{background:var(--white);border:2.5px solid var(--deep)}
.tile h3{font-weight:400;font-size:10.5px;color:var(--navy);margin-bottom:5px}
.tile p{font-size:5.4px;line-height:1.5;color:#666}
.notch-down::after,.notch-up::after{content:"";position:absolute;left:50%;width:11px;height:11px;background:var(--yellow);transform:translateX(-50%) rotate(45deg)}
.notch-down::after{bottom:-5px}
.notch-up::after{top:-5px}
/* flow slide */
.step h3{font-weight:400;font-size:12px;color:var(--navy);margin-bottom:4px}
/* circle slide */
.team-card{position:absolute;top:64px;width:150px;text-align:center}
.ring{width:94px;height:94px;margin:0 auto;border:1.5px solid var(--ink);border-radius:50%;padding:4px}
.ring .photo{position:static;width:100%;height:100%;border-radius:50%;background:var(--hall)}
.team-card h3{margin-top:22px;font-weight:400;font-size:14px;color:var(--navy);letter-spacing:.3px}
.team-card p{margin-top:4px;font-size:4.6px;line-height:1.45;color:#333}
/* two-photo slide */
.bullet{position:absolute;left:22px;width:200px}
.bullet .badge{position:absolute;left:0;top:2px;width:12px;height:12px;border-radius:50%;background:var(--yellow);font-size:3.8px;font-weight:700;display:flex;align-items:center;justify-content:center}
.bullet h4{margin-left:21px;font-weight:500;font-size:9px;color:var(--ink)}
.bullet p{margin-left:21px;margin-top:3px;font-size:6.6px;line-height:1.6;color:#444}
.number-badge{position:absolute;width:34px;height:34px;border-radius:50%;background:var(--yellow);border:3px solid var(--white);font-size:10px;font-weight:600;display:flex;align-items:center;justify-content:center}
</style>
</head>
<body>

<!-- Cover -->
<section class="slide" style="left:69px;top:118px">
  <div class="photo" style="left:18px;top:15px;width:484px;height:158px" role="img" aria-label="City skyline photograph with high-rise towers under a pale sky"></div>
  <div class="abs" style="left:366px;top:0;width:111px;height:32px;background:var(--dark)"></div>
  <div class="abs" style="left:0;top:183px;width:16px;height:61px;background:var(--yellow)"></div>
  <div class="cover-title">LOREN</div>
  <div class="cover-sub">IPSUM</div>
  <div class="dots" style="left:28px;top:258px;width:106px;height:13px;background-size:8.8px 7px"></div>
  <div class="logo-box">logo</div>
</section>

<!-- Tile grid -->
<section class="slide" style="left:622px;top:118px">
  <div class="header-title">LOREN IPSUM</div>
  <div class="header-rule"></div>
  <div class="dots" style="left:408px;top:10px"></div>
  <div class="tile-grid">
    <div class="tile is-yellow notch-down">
      <svg width="48" height="48" viewBox="0 0 48 48" fill="none" stroke="var(--deep)" stroke-width="2"><circle cx="22" cy="26" r="17"/><circle cx="22" cy="26" r="11"/><circle cx="22" cy="26" r="5"/><path d="M22 26 L40 8 M36 6 L40 8 L42 12"/></svg>
    </div>
    <div class="tile is-white"><h3>02 Title Here</h3><p>Lorem ipsum dolor sit amet, consectetuer adipiscing elit, sed diam nonummy nibh euismod tincidunt ut.</p></div>
    <div class="tile is-yellow notch-down">
      <svg width="48" height="44" viewBox="0 0 48 44" fill="none" stroke="var(--deep)" stroke-width="2" stroke-linejoin="round"><path d="M4 18 L14 10 L22 14 L30 10 L44 18 L34 30 L26 38 L14 28 Z"/><path d="M22 14 L16 20 L20 22 L28 16"/><path d="M18 26 L22 30 M22 24 L27 29 M26 22 L31 27"/><path d="M24 2 V6 M16 4 L18 7 M32 4 L30 7"/></svg>
    </div>
    <div class="tile is-white"><h3>04 Title Here</h3><p>Lorem ipsum dolor sit amet, consectetuer adipiscing elit, sed diam nonummy nibh euismod tincidunt ut.</p></div>
    <div class="tile is-white"><h3>01 Title Here</h3><p>Lorem ipsum dolor sit amet, consectetuer adipiscing elit, sed diam nonummy nibh euismod tincidunt ut.</p></div>
    <div class="tile is-yellow notch-up">
      <svg width="50" height="48" viewBox="0 0 50 48" fill="none" stroke="var(--deep)" stroke-width="2"><path d="M4 46 H46"/><rect x="8" y="34" width="6" height="12"/><rect x="18" y="28" width="6" height="18"/><rect x="28" y="30" width="6" height="16"/><rect x="38" y="22" width="6" height="24"/><path d="M8 28 L20 20 L30 24 L40 14"/><circle cx="40" cy="8" r="6"/><path d="M40 5 V11"/></svg>
    </div>
    <div class="tile is-white"><h3>03 Title Here</h3><p>Lorem ipsum dolor sit amet, consectetuer adipiscing elit, sed diam nonummy nibh euismod tincidunt ut.</p></div>
    <div class="tile is-yellow notch-up">
      <svg width="50" height="46" viewBox="0 0 50 46" fill="none" stroke="var(--deep)" stroke-width="2"><rect x="16" y="2" width="18" height="11" rx="1"/><circle cx="10" cy="18" r="4"/><circle cx="40" cy="18" r="4"/><path d="M3 36 V28 Q3 23 10 23 Q17 23 17 28 V36 M33 36 V28 Q33 23 40 23 Q47 23 47 28 V36"/><path d="M14 30 H36 M20 30 V44 M30 30 V44"/></svg>
    </div>
  </div>
  <div class="footer"><span class="logo-text">logo</span><span class="page-no">04</span></div>
</section>

<!-- Text with diamond photo -->
<section class="slide" style="left:69px;top:453px">
  <div class="abs" style="left:390px;top:0;width:130px;height:260px;background:var(--dark)"></div>
  <div class="header-title">LOREN IPSUM</div>
  <div class="abs" style="left:28px;top:32px;width:340px;height:1px;background:var(--ink)"></div>
  <div class="abs" style="left:366px;top:30px;width:5px;height:5px;background:var(--ink)"></div>
  <div class="dots" style="left:408px;top:10px;background-image:radial-gradient(circle,var(--white) 0.8px,transparent 1.1px)"></div>
  <p class="body-text abs" style="left:33px;top:58px;width:215px">Lorem ipsum dolor sit amet, consectetuer adipiscing elit, sed diam nonummy nibh euismod tincidunt ut laoreet dolore magna aliquam erat volutpat.</p>
  <svg class="abs" style="left:32px;top:120px" width="30" height="30" viewBox="0 0 30 30" fill="none" stroke="var(--deep)" stroke-width="1.4"><circle cx="13" cy="17" r="11"/><circle cx="13" cy="17" r="7"/><circle cx="13" cy="17" r="3"/><path d="M13 17 L26 4 M23 3 L26 4 L27 7"/></svg>
  <div class="abs" style="left:69px;top:120px;width:2px;height:28px;background:var(--yellow)"></div>
  <p class="body-text abs" style="left:83px;top:120px;width:190px">Lorem ipsum dolor sit amet, consectetuer adipiscing elit, sed diam nonummy nibh euismod tincidunt ut laoreet dolore magna aliquam.</p>
  <svg class="abs" style="left:32px;top:173px" width="30" height="32" viewBox="0 0 30 32" fill="none" stroke="var(--deep)" stroke-width="1.4"><path d="M2 30 H28 M4 30 V24 H12 V18 H20 V30"/><path d="M8 2 V12 M8 2 H14 L12 5 L14 8 H8"/><circle cx="14" cy="11" r="2"/><path d="M14 13 L15 18 M12 15 L17 14"/></svg>
  <div class="abs" style="left:69px;top:173px;width:2px;height:28px;background:var(--yellow)"></div>
  <p class="body-text abs" style="left:83px;top:173px;width:190px">Lorem ipsum dolor sit amet, consectetuer adipiscing elit, sed diam nonummy nibh euismod tincidunt ut laoreet dolore magna aliquam.</p>
  <svg class="abs" style="left:265px;top:30px" width="250" height="235" viewBox="0 0 250 235">
    <defs><linearGradient id="skyTone" x1="0" y1="0" x2="0" y2="1"><stop offset="0" stop-color="#c9d6e3"/><stop offset=".5" stop-color="#9aaabb"/><stop offset="1" stop-color="#3b4757"/></linearGradient></defs>
    <polygon points="126,7 236,116 126,225 16,116" fill="url(#skyTone)" role="img" aria-label="City skyline photograph cropped into a diamond"/>
    <polyline points="46,83 12,116 46,149" fill="none" stroke="var(--yellow)" stroke-width="5"/>
    <polyline points="206,83 240,116 206,149" fill="none" stroke="var(--yellow)" stroke-width="7"/>
  </svg>
  <div class="footer"><span class="logo-text">logo</span><span class="page-no">02</span></div>
</section>

<!-- Process curve -->
<section class="slide" style="left:622px;top:454px">
  <div class="header-title">LOREN IPSUM</div>
  <div class="header-rule"></div>
  <div class="dots" style="left:408px;top:10px"></div>
  <svg class="abs" style="left:0;top:0" width="520" height="260" viewBox="0 0 520 260" fill="none">
    <path d="M150 81 H176 V93 H185 M150 143 H176 V155 H195 M343 133 H366 M345 133 V145 H343 M261 183 V196" stroke="#999" stroke-width="0.6"/>
    <path d="M212 74 V114" stroke="#8c8c8c" stroke-width="37"/>
    <path d="M212 114 A47 47 0 0 0 235.5 154.7" stroke="#6e6e6e" stroke-width="37"/>
    <path d="M235.5 154.7 A47 47 0 0 0 282.5 154.7" stroke="#5a5a5a" stroke-width="37"/>
    <path d="M282.5 154.7 A47 47 0 0 0 306 114" stroke="#454545" stroke-width="37"/>
    <path d="M306 114 C306 85 316 78 368 78" stroke="var(--deep)" stroke-width="37"/>
    <path d="M194 114 H230 M219 139 L241 125 M259 143 V170 M290 128 L316 146" stroke="var(--white)" stroke-width="1.5"/>
    <polygon points="366,48 397,78 366,108" fill="var(--yellow)"/>
    <g stroke="var(--white)" stroke-width="1.1">
      <circle cx="212" cy="95" r="7"/><circle cx="212" cy="95" r="3.5"/><path d="M212 95 L219 88"/>
      <path d="M223 140 L229 134 L235 138 L229 145 Z"/>
      <path d="M252 155 V150 M256 155 V146 M260 155 V148 M264 155 V143 M250 155 H267"/>
      <circle cx="298" cy="132" r="4.5"/><path d="M298 124 V127 M298 137 V140 M290 132 H293 M303 132 H306"/>
    </g>
  </svg>
  <div class="step abs" style="left:50px;top:72px;width:120px"><h3>01 Title Here</h3><p class="tiny">Lorem ipsum dolor sit amet, consectetuer adipiscing elit, sed diam nonummy</p></div>
  <div class="step abs" style="left:50px;top:134px;width:120px"><h3>02 Title Here</h3><p class="tiny">Lorem ipsum dolor sit amet, consectetuer adipiscing elit, sed diam nonummy</p></div>
  <div class="step abs" style="left:384px;top:123px;width:120px"><h3>04 Title Here</h3><p class="tiny">Lorem ipsum dolor sit amet, consectetuer adipiscing elit, sed diam nonummy</p></div>
  <div class="step abs" style="left:221px;top:201px;width:120px"><h3>03 Title Here</h3><p class="tiny">Lorem ipsum dolor sit amet, consectetuer adipiscing elit, sed diam.</p></div>
  <div class="footer"><span class="logo-text">logo</span><span class="page-no">05</span></div>
</section>

<!-- Three circles -->
<section class="slide" style="left:69px;top:788px">
  <div class="header-title">LOREN IPSUM</div>
  <div class="header-rule"></div>
  <div class="dots" style="left:408px;top:10px"></div>
  <div class="team-card" style="left:26px">
    <div class="ring"><div class="photo" role="img" aria-label="Warehouse interior photograph"></div></div>
    <h3>LOREN IPSUM</h3>
    <p>Lorem Ipsum is simply dummy text of the printing and typesetting industry. Lorem Ipsum has been the industry's standard dummy text ever since the 1500s, when an unknown printer took a galley of type and scrambled it to make a type specimen book.</p>
  </div>
  <div class="team-card" style="left:185px">
    <div class="ring"><div class="photo" role="img" aria-label="Warehouse interior photograph"></div></div>
    <h3>LOREN IPSUM</h3>
    <p>Lorem Ipsum is simply dummy text of the printing and typesetting industry. Lorem Ipsum has been the industry's standard dummy text ever since the 1500s, when an unknown printer took a galley of type and scrambled it to make a type specimen book.</p>
  </div>
  <div class="team-card" style="left:344px">
    <div class="ring"><div class="photo" role="img" aria-label="Warehouse interior photograph"></div></div>
    <h3>LOREN IPSUM</h3>
    <p>Lorem Ipsum is simply dummy text of the printing and typesetting industry. Lorem Ipsum has been the industry's standard dummy text ever since the 1500s, when an unknown printer took a galley of type and scrambled it to make a type specimen book.</p>
  </div>
  <div class="footer"><span class="logo-text">logo</span><span class="page-no">03</span></div>
</section>

<!-- Two photos -->
<section class="slide" style="left:622px;top:790px">
  <div class="abs" style="left:389px;top:0;width:131px;height:260px;background:var(--dark)"></div>
  <div class="header-title">LOREN IPSUM</div>
  <div class="abs" style="left:28px;top:32px;width:336px;height:1px;background:var(--ink)"></div>
  <div class="abs" style="left:362px;top:30px;width:5px;height:5px;background:var(--ink)"></div>
  <p class="body-text abs" style="left:16px;top:55px;width:193px;text-align:justify;font-size:6.6px;line-height:1.65">It is a long established fact that a reader will be distracted by the readable content of a page when looking at its layout. It is a long established fact that a reader will be distracted by the readable content of a page when looking at its layout.</p>
  <div class="bullet" style="top:134px"><span class="badge">01</span><h4>Simple Text One</h4><p>Lorem Ipsum is simply dummy text of the printing and typesetting industry.</p></div>
  <div class="bullet" style="top:184px"><span class="badge">02</span><h4>Simple Text Two</h4><p>Lorem Ipsum is simply dummy text of the printing and typesetting industry.</p></div>
  <div class="photo" style="left:214px;top:104px;width:133px;height:134px;border-radius:10px" role="img" aria-label="City skyline photograph"></div>
  <div class="photo" style="left:359px;top:104px;width:133px;height:134px;border-radius:10px" role="img" aria-label="City skyline photograph"></div>
  <div class="number-badge" style="left:231px;top:86px">01</div>
  <div class="number-badge" style="left:373px;top:86px">02</div>
  <div class="footer"><span class="logo-text">logo</span><span class="page-no">03</span></div>
</section>

</body>
</html>
```